I am a surgeon that operates on gynaecological cancer. Wish a design and logo for letter head.

Design should include my name: Dr. Kiran Mudaly, qualifications: FTELSWOB, CGO. and state that I am a Gynaecological Oncologist and Advanced Laparoscopic Surgeon.
As for a logo. As all cancer is related to DNA, I think that that double helix could be used to symbolise a female shape, exaggerating the abdomen to suggest a mass.

Reason: Extended to view changes I have asked for.

```html
<!DOCTYPE html>
<html lang="en">
<head>
<meta charset="utf-8">
<title>Dr Kiran Mudaly – Letterhead</title>
<link rel="stylesheet" href="https://fonts.googleapis.com/css2?family=EB+Garamond:wght@400&family=Arimo:wght@400&display=swap">
<style>
  :root {
    --backdrop: #e6e7e9;
    --paper: #ffffff;
    --brand-blue: #0b5c93;
    --brand-orange: #f28a35;
    --ink: #3a3a3a;
    --watermark: #f4f4f4;
  }
  html, body {
    margin: 0;
    padding: 0;
    width: 1200px;
    height: 1000px;
    overflow: hidden;
    background: var(--backdrop);
  }
  .canvas {
    position: relative;
    width: 1200px;
    height: 1000px;
  }
  .sheet {
    position: absolute;
    top: 148px;
    width: 498px;
    height: 704px;
    background: var(--paper);
  }
  .sheet--classic { left: 87px; }
  .sheet--caps { left: 615px; }

  .masthead {
    position: absolute;
    top: 32px;
    left: 248px;
    width: 215px;
    height: 48px;
  }
  .masthead__mark {
    position: absolute;
    left: 0;
    top: 0;
    width: 48px;
    height: 48px;
    background: var(--brand-orange);
  }
  .masthead__name {
    position: absolute;
    left: 58px;
    top: 4px;
    margin: 0;
    font-family: "EB Garamond", Garamond, serif;
    font-weight: 400;
    font-size: 22px;
    line-height: 26px;
    color: var(--brand-blue);
    white-space: nowrap;
  }
  .masthead__credentials {
    position: absolute;
    right: 5px;
    top: 34px;
    margin: 0;
    font-family: "Arimo", Arial, sans-serif;
    font-size: 7px;
    letter-spacing: 0.3px;
    color: var(--brand-blue);
  }

  .specialty {
    position: absolute;
    margin: 0;
    font-family: "Arimo", Arial, sans-serif;
    color: var(--ink);
  }
  .specialty--classic {
    top: 91px;
    right: 40px;
    text-align: right;
    font-size: 8.5px;
    line-height: 12px;
  }
  .specialty--classic .specialty__line:first-child { letter-spacing: 1.3px; }
  .specialty--caps {
    top: 86px;
    left: 270px;
    width: 170px;
    margin-left: -85px;
    text-align: center;
    font-size: 7.5px;
    line-height: 11px;
    text-transform: uppercase;
  }
  .specialty__line { display: block; }

  .watermark {
    position: absolute;
    left: 183px;
    top: 220px;
    width: 120px;
    height: 335px;
    background: linear-gradient(180deg, var(--paper), var(--watermark) 30%, var(--watermark) 70%, var(--paper));
    border-radius: 50px;
  }
</style>
</head>
<body>
<main class="canvas">
  <section class="sheet sheet--classic" aria-label="Letterhead, sentence-case version">
    <header class="masthead">
      <span class="masthead__mark"></span>
      <h1 class="masthead__name">Dr Kiran Mudaly</h1>
      <p class="masthead__credentials">FTELSWOB, CGO.</p>
    </header>
    <p class="specialty specialty--classic">
      <span class="specialty__line">Gynaecological Oncologist</span>
      <span class="specialty__line">and Advanced Laparoscopic Surgeon</span>
    </p>
    <div class="watermark" role="img" aria-label="Faint brand symbol watermark area"></div>
  </section>

  <section class="sheet sheet--caps" aria-label="Letterhead, uppercase version">
    <header class="masthead">
      <span class="masthead__mark"></span>
      <h1 class="masthead__name">Dr Kiran Mudaly</h1>
      <p class="masthead__credentials">FTELSWOB, CGO.</p>
    </header>
    <p class="specialty specialty--caps">
      <span class="specialty__line">Gynaecological Oncologist</span>
      <span class="specialty__line">&amp; Advanced Laparoscopic Surgeon</span>
    </p>
    <div class="watermark" role="img" aria-label="Faint brand symbol watermark area"></div>
  </section>
</main>
</body>
</html>
```